Kelekeleoliolimaiwaipeleke Fish Package

We need a package design for our Kelekeleoliolimaiwaipeleke Fish (not Bravlin fish). We plan to sell them at Hawaii stores to start and them take them to the mainland. We are looking for a package design that includes the front with a Kelekeleoliolimaiwaipeleke Fish (not a photo) and a back design with a photo of the fish (we will supply), information about the fish and nutrition information.

Target Market(s)

Premium market

Colors

Designer to choose colors to be used in the design.

Requirements
Must have
• See attached overview - also, it must include our logo (which we will provide)
Nice to have
• See attached overview

```html
<!DOCTYPE html>
<html lang="en">
<head>
<meta charset="UTF-8">
<title>Kelekeleoliolimaiwaipeleke Fish – Pouch Front</title>
<link rel="stylesheet" href="https://fonts.googleapis.com/css2?family=Antonio:wght@300&family=Josefin+Sans:wght@300;600&family=Montserrat:wght@500;600&display=swap">
<style>
  :root {
    --bg: #ffffff;
    --coral: #e27a78;
    --sun: #e8c95e;
    --cream: #f1ece1;
    --cream-label: #efe9dc;
    --copper: #ad5f1e;
    --copper-light: #c6874a;
    --rule: #b9a48c;
    --teal: #2fb8b0;
    --blush: #f0a3a3;
    --leaf: #2f6a4a;
  }
  * { box-sizing: border-box; margin: 0; padding: 0; }
  html, body {
    width: 1200px; height: 1200px; overflow: hidden;
    background: var(--bg);
  }
  .pouch {
    position: absolute; left: 234px; top: 150px;
    width: 732px; height: 942px;
    background: var(--cream);
    overflow: hidden;
  }
  .pouch__top-band {
    position: absolute; left: 0; top: 0; width: 100%; height: 90px;
    background: var(--coral);
  }
  .pouch__hang-hole {
    position: absolute; left: 308px; top: 56px; width: 116px; height: 18px;
    border-radius: 9px; background: var(--bg);
  }
  .pouch__side-strip {
    position: absolute; top: 90px; width: 26px; height: 160px;
    background: var(--sun);
  }
  .pouch__side-strip--left { left: 0; }
  .pouch__side-strip--right { right: 0; }
  .label {
    position: absolute; left: 26px; top: 90px; width: 680px; height: 496px;
    background: var(--cream-label);
    text-align: center; color: var(--copper);
  }
  .brand-name {
    position: absolute; left: 0; right: 0; top: 66px;
    font-family: "Josefin Sans", sans-serif; font-weight: 600;
    font-size: 64px; letter-spacing: 5px; line-height: 1;
  }
  .ruled {
    position: absolute; left: 16px; right: 16px;
    display: flex; align-items: center; gap: 20px;
    font-family: "Montserrat", sans-serif; font-weight: 600;
    letter-spacing: 3px; line-height: 1;
  }
  .ruled::before, .ruled::after {
    content: ""; flex: 1; height: 1px; background: var(--rule);
  }
  .tier { top: 150px; font-size: 25px; }
  .tagline { top: 308px; font-size: 22px; }
  .product-name {
    position: absolute; left: 0; right: 0; top: 216px;
    font-family: "Antonio", sans-serif; font-weight: 300;
    font-size: 58px; letter-spacing: -0.5px; line-height: 1;
    white-space: nowrap;
  }
  .flavours {
    position: absolute; left: 0; right: 0; top: 360px;
    font-family: "Montserrat", sans-serif; font-weight: 500;
    font-size: 20px; letter-spacing: 2.5px; line-height: 1;
    color: var(--copper-light);
  }
  .flavours__and { font-size: 16px; text-decoration: underline; }
  .net-weight {
    position: absolute; left: 0; right: 0; top: 414px;
    display: flex; justify-content: center; align-items: center; gap: 12px;
  }
  .net-weight__label {
    font-family: "Montserrat", sans-serif; font-weight: 600;
    font-size: 13px; letter-spacing: 1px; line-height: 1.25; text-align: left;
  }
  .net-weight__value {
    font-family: "Josefin Sans", sans-serif; font-weight: 300;
    font-size: 42px; line-height: 1; padding-top: 6px;
  }
  .pattern-area {
    position: absolute; left: 38px; top: 586px; width: 656px; height: 356px;
    background:
      radial-gradient(ellipse 22% 30% at 50% 0%, var(--sun) 0%, var(--sun) 60%, transparent 100%),
      radial-gradient(ellipse 38% 60% at 50% 10%, var(--blush) 0%, var(--coral) 55%, transparent 100%),
      radial-gradient(ellipse 50% 85% at 50% 15%, var(--teal) 55%, var(--leaf) 80%, transparent 100%),
      transparent;
  }
</style>
</head>
<body>
  <div class="pouch">
    <div class="pouch__top-band"></div>
    <div class="pouch__hang-hole"></div>
    <div class="pouch__side-strip pouch__side-strip--left"></div>
    <div class="pouch__side-strip pouch__side-strip--right"></div>

    <div class="label">
      <div class="brand-name">LANI KOLU</div>
      <div class="ruled tier">PREMIUM</div>
      <h1 class="product-name">KELEKELEOLIOLIMAIWAIPELEKE FISH</h1>
      <div class="ruled tagline">A HAWAIIAN TREAT</div>
      <p class="flavours">PINEAPPLE, CITRUS <span class="flavours__and">AND</span> RASPBERRY</p>
      <div class="net-weight">
        <span class="net-weight__label">NET<br>WT:</span>
        <span class="net-weight__value">5.0 oz</span>
      </div>
    </div>

    <div class="pattern-area" role="img" aria-label="Tropical mandala pattern of coral petals, yellow rays, teal shapes and dark green leaves"></div>
  </div>
</body>
</html>
```